High end Electrical/home automation Business Card

Need a card for a high end electrical and home automation company utilising the existing logo.
Phone
Email
Website

Like black look with raised detail. Don’t necessarily need to keep colour of logo it could be made grayscale or white etc

Target Market(s)

High end clients

Contact Information for Business Card

Ridgeline Electrical

Requirements
Must have
• Logo, phone, email, website, address

High end look
Nice to have
• Black background card
Raised font
Should not have
• Lots of colour

```html
<!DOCTYPE html>
<html lang="en">
<head>
<meta charset="utf-8">
<title>Ridgeline Electrical – Business Card</title>
<link rel="stylesheet" href="https://fonts.googleapis.com/css2?family=Arimo:wght@400;700&display=swap">
<style>
  :root {
    --backdrop: #2a2a2c;
    --card-dark: #3a3a3c;
    --card-dark-edge: #2b2b2d;
    --card-light: #ffffff;
    --ink: #2d2d2f;
    --ink-soft: #444446;
    --brand-blue: #1a8fd8;
    --on-dark: #ffffff;
  }
  * { box-sizing: border-box; margin: 0; padding: 0; }
  html, body {
    width: 1200px; height: 900px; overflow: hidden;
    background: var(--backdrop);
    font-family: "Arimo", Arial, sans-serif;
  }
  .canvas { position: relative; width: 1200px; height: 900px; }

  .card {
    position: absolute;
    width: 660px; height: 377px;
    border-radius: 26px;
    overflow: hidden;
    box-shadow: 0 18px 40px rgba(0,0,0,.45);
  }

  /* Back: dark side */
  .card--back {
    left: 90px; top: 50px;
    background: linear-gradient(160deg, #434345 0%, var(--card-dark) 55%, var(--card-dark-edge) 100%);
    border-bottom: 6px solid #1f1f21;
    display: flex; flex-direction: column; align-items: center; justify-content: center;
    color: var(--on-dark);
  }
  .back-brand {
    display: flex; align-items: center; gap: 16px;
    font-weight: 700; font-size: 42px; letter-spacing: -0.5px;
  }
  .brand-dot {
    width: 26px; height: 26px; border-radius: 50%;
    background: var(--brand-blue);
  }
  .back-web {
    margin-top: 34px;
    font-size: 17px; letter-spacing: 5px;
  }

  /* Front: light side */
  .card--front {
    left: 450px; top: 470px;
    background: var(--card-light);
    border-bottom: 8px solid var(--brand-blue);
    color: var(--ink);
  }
  .front-brand {
    position: absolute; right: 60px; top: 62px;
    display: flex; align-items: center; gap: 12px;
    font-weight: 700; font-size: 32px; letter-spacing: -0.4px; color: var(--ink);
  }
  .front-brand .brand-dot { width: 20px; height: 20px; }
  .address {
    position: absolute; right: 60px; top: 224px;
    text-align: right; font-size: 17px; line-height: 1.3; color: var(--ink-soft);
  }
  .person {
    position: absolute; left: 40px; right: 50px; top: 158px;
  }
  .person-name {
    font-weight: 700; font-size: 30px; color: var(--brand-blue); letter-spacing: .3px;
  }
  .role-row {
    display: flex; align-items: center; gap: 12px; margin-top: 2px;
  }
  .person-role { font-size: 19px; color: var(--ink-soft); flex: none; }
  .rule { flex: 1; height: 1.5px; background: var(--ink); }
  .contact-list {
    list-style: none; margin-top: 14px;
    font-size: 20px; color: var(--ink); line-height: 1.45;
  }
  .contact-list li { display: flex; align-items: center; gap: 14px; }
  .contact-list svg { width: 20px; height: 20px; flex: none; }
  .contact-list .accent { color: var(--brand-blue); }
</style>
</head>
<body>
<main class="canvas">

  <section class="card card--back" aria-label="Card back">
    <div class="back-brand"><span class="brand-dot"></span><span>Ridgeline Electrical</span></div>
    <p class="back-web">www.ridgelineelectrical.com</p>
  </section>

  <section class="card card--front" aria-label="Card front">
    <div class="front-brand"><span class="brand-dot"></span><span>Ridgeline Electrical</span></div>
    <p class="address">418 Alder Lane, Fairview<br>OR, 97024</p>

    <div class="person">
      <h1 class="person-name">Marcus Hale</h1>
      <div class="role-row">
        <p class="person-role">Manager</p>
        <span class="rule"></span>
      </div>
      <ul class="contact-list">
        <li>
          <svg viewBox="0 0 24 24" aria-hidden="true"><path fill="#1a8fd8" d="M6.6 10.8a15.1 15.1 0 0 0 6.6 6.6l2.2-2.2a1 1 0 0 1 1-.25 11.4 11.4 0 0 0 3.6.57 1 1 0 0 1 1 1V20a1 1 0 0 1-1 1A17 17 0 0 1 3 4a1 1 0 0 1 1-1h3.5a1 1 0 0 1 1 1c0 1.25.2 2.450.57 3.57a1 1 0 0 1-.25 1z"/></svg>
          <span>555-318-4720</span>
        </li>
        <li>
          <svg viewBox="0 0 24 24" aria-hidden="true"><rect x="3" y="5.5" width="18" height="13" rx="1.5" fill="none" stroke="#1a8fd8" stroke-width="2"/><path d="M3.5 6.5 12 13l8.5-6.5" fill="none" stroke="#1a8fd8" stroke-width="2"/></svg>
          <span>marcus@ridgelinemail.com</span>
        </li>
        <li>
          <svg viewBox="0 0 24 24" aria-hidden="true"><g fill="none" stroke="#1a8fd8" stroke-width="1.8"><circle cx="12" cy="12" r="9"/><ellipse cx="12" cy="12" rx="4" ry="9"/><path d="M3 12h18M4.5 7.5h15M4.5 16.5h15"/></g></svg>
          <span>www.<span class="accent">ridgelineelectrical</span>.com</span>
        </li>
      </ul>
    </div>
  </section>

</main>
</body>
</html>
```